Makeup Artist

Hi I am makeup artist I attached the business card that I found on the net love the design.
I would love something like this simple but looking expensive.
I want double side business card. Front my full name. my phone number, email address and facebook and my next appointment is... on the other side.
Thank you :)

Hello I change my Facebook account - Makeup by Liora, if you could please update your designs , thank you

Target Market(s)

high end clientele

Industry/Entity Type

Business

Colors
ec2027
ffc214
33b7a4
6b449b
e34197
9bcb3c
f37122
a64599

Requirements
Must have
• bright colours
Should not have
• brushes or whole lipsticks

```html
<!DOCTYPE html>
<html lang="en">
<head>
<meta charset="utf-8">
<title>Liora Vandermeer – Business Card</title>
<link rel="stylesheet" href="https://fonts.googleapis.com/css2?family=Dancing+Script:wght@400;600&display=swap">
<style>
  :root {
    --sheet: #ffffff;
    --label: #3a3a3a;
    --teal: #33b7a4;
    --red: #ec2027;
    --yellow: #ffc214;
    --orange: #f37122;
    --purple: #6b449b;
    --white: #ffffff;
    --edge: #c9a27a;
    --script: 'Dancing Script', cursive;
  }
  html, body {
    margin: 0;
    padding: 0;
    overflow: hidden;
    background: var(--sheet);
  }
  .sheet {
    position: relative;
    width: 1200px;
    height: 848px;
    background: var(--sheet);
    overflow: hidden;
    font-family: var(--script);
  }
  .side-label, .dimension {
    position: absolute;
    color: var(--label);
    font-size: 17px;
    line-height: 1;
    transform: translateX(-50%);
  }
  .side-label--front { left: 368px; top: 192px; }
  .side-label--back  { left: 822px; top: 192px; }
  .dimension--height { left: 134px; top: 380px; }
  .dimension--width  { left: 367px; top: 516px; }

  .card {
    position: absolute;
    top: 292px;
    width: 362px;
    height: 181px;
    overflow: hidden;
    box-shadow: inset 0 0 0 1px var(--edge);
  }
  .card--front { left: 203px; }
  .card--back  { left: 652px; }

  .card__photo {
    position: absolute;
    inset: 0;
  }
  .card--front .card__photo {
    background:
      radial-gradient(circle at 78% 30%, rgba(255,194,20,.75) 0 12%, transparent 30%),
      radial-gradient(circle at 88% 70%, rgba(150,30,35,.85) 0 14%, transparent 32%),
      radial-gradient(circle at 40% 20%, rgba(155,203,60,.45) 0 10%, transparent 28%),
      radial-gradient(circle at 15% 45%, rgba(110,60,40,.7) 0 8%, transparent 20%),
      radial-gradient(circle at 55% 75%, rgba(243,113,34,.5) 0 12%, transparent 32%),
      linear-gradient(120deg, #3b3f6e 0%, #6b5a6e 35%, #9a8a55 60%, #6d4a3a 100%);
  }
  .card--back .card__photo {
    background:
      radial-gradient(circle at 70% 25%, rgba(255,194,20,.6) 0 10%, transparent 28%),
      radial-gradient(circle at 85% 55%, rgba(155,203,60,.45) 0 10%, transparent 26%),
      radial-gradient(circle at 32% 65%, rgba(150,30,40,.85) 0 10%, transparent 22%),
      radial-gradient(circle at 10% 85%, rgba(20,20,25,.9) 0 9%, transparent 20%),
      radial-gradient(circle at 50% 30%, rgba(227,65,151,.35) 0 10%, transparent 28%),
      linear-gradient(120deg, #3a3d6b 0%, #6a5b70 35%, #9b8c58 65%, #6a5f3f 100%);
  }

  .card__text { position: absolute; margin: 0; line-height: 1; white-space: nowrap; }

  .card__name   { left: 11px; top: 16px; font-size: 34px; color: var(--teal); font-weight: 400; }
  .card__role   { left: 128px; top: 58px; font-size: 12px; color: var(--red); }
  .card__phone  { left: 13px; top: 120px; font-size: 23px; color: var(--red); }
  .card__email  { left: 13px; top: 152px; font-size: 11px; color: var(--white); font-weight: 600; }

  .card__social {
    position: absolute;
    left: 146px;
    top: 128px;
    display: flex;
    align-items: center;
    gap: 4px;
  }
  .card__social-mark {
    width: 12px;
    height: 12px;
    background: var(--teal);
  }
  .card__social-name { font-size: 11px; color: var(--white); font-weight: 600; }
  .card__social-handle { left: 146px; top: 152px; font-size: 9px; color: var(--teal); }

  .card__quote  { left: 30px; top: 30px; font-size: 14px; color: var(--yellow); }
  .card__author { left: 262px; top: 62px; font-size: 11px; color: var(--white); }
  .card__prompt { left: 187px; top: 143px; font-size: 14px; color: var(--yellow); }
</style>
</head>
<body>
<main class="sheet">
  <div class="side-label side-label--front">Front</div>
  <div class="side-label side-label--back">Back</div>
  <div class="dimension dimension--height">45 mm</div>
  <div class="dimension dimension--width">90 mm</div>

  <section class="card card--front">
    <div class="card__photo" role="img" aria-label="Soft colourful bokeh photo with red lipstick pieces and a smudge of makeup"></div>
    <h1 class="card__text card__name">Liora Vandermeer</h1>
    <p class="card__text card__role">Freelance Makeup Artist</p>
    <p class="card__text card__phone">0412558093</p>
    <p class="card__text card__email">lioravandermeer@mail.com</p>
    <div class="card__social">
      <span class="card__social-mark"></span>
      <span class="card__social-name">Makeup by Liora</span>
    </div>
    <p class="card__text card__social-handle">Makeup by Liora</p>
  </section>

  <section class="card card--back">
    <div class="card__photo" role="img" aria-label="Soft colourful bokeh photo with a spilled bottle of red nail polish"></div>
    <p class="card__text card__quote">“I love the confidence that makeup gives me.”</p>
    <p class="card__text card__author">by Tessa Marlowe</p>
    <p class="card__text card__prompt">“My next appointment is...”</p>
  </section>
</main>
</body>
</html>
```